Calder Pizza - Takeout Menu Design

We are looking for a takeout menu design.
We are looking for a( 5" x 8.5" DOUBLE SIDED) flyer with our available pizza flavors
Must be easy to ready and not "busy"

Must include our logo (attached)
website: www.calderpizza.ca
address:
Fenwick Ridge Plaza
417, 318 9 Avenue SW
and the following details:
Visit our website for our complete appetizer, pasta, salad and catering menu.

Winner of this contest will also be offered to create a few print designs via printhive.

Please do not hesitate to ask any questions.

Target Market(s)

Business / Office clientele

Industry/Entity Type

Pizza place / specializing in corporate orders

Requirements
Must have
• Easy to read
Should not have
• Can not be busy or cluttered

```html
<!DOCTYPE html>
<html lang="en">
<head>
<meta charset="utf-8">
<title>Calder Pizza – Take-Out Menu</title>
<link href="https://fonts.googleapis.com/css2?family=Open+Sans:wght@300;400;600;700&display=swap" rel="stylesheet">
<style>
  :root {
    --backdrop: #9a9a9a;
    --paper: #f6f3ee;
    --ink: #1c1c1c;
    --brand-red: #c0311f;
    --rule: #cfcac3;
    --white: #ffffff;
    --crust-light: #f3b04a;
    --crust-dark: #c7521f;
  }
  * { box-sizing: border-box; margin: 0; padding: 0; }
  html, body {
    width: 1200px; height: 1000px; overflow: hidden;
    background: var(--backdrop);
    font-family: "Open Sans", Arial, sans-serif;
    color: var(--ink);
  }
  .canvas { position: relative; width: 1200px; height: 1000px; }

  .page {
    position: absolute; top: 121px; width: 491px; height: 759px;
    background: var(--paper); overflow: hidden;
  }
  .page--front { left: 80px; }
  .page--back { left: 612px; }

  /* Front */
  .wordmark {
    position: absolute; left: 104px; top: 0;
    color: var(--brand-red); font-weight: 300; line-height: 1;
    letter-spacing: 1px;
  }
  .page--front .wordmark { left: 24px; top: 22px; font-size: 46px; }
  .wordmark span { display: block; }
  .wordmark .line-two { padding-left: 30px; }

  .pizza-photo {
    position: absolute; left: 246px; top: 0; width: 245px; height: 325px;
    background: radial-gradient(circle at 65% 55%, var(--crust-light) 0%, #e98a33 55%, var(--crust-dark) 100%);
    border-radius: 0 0 0 60%;
  }

  .section-title {
    position: absolute; left: 19px;
    color: var(--brand-red); font-weight: 400; font-size: 14.5px;
  }
  .section-title--classic { top: 126px; }
  .section-title--specialty { top: 320px; }

  .classic-list {
    position: absolute; left: 19px; top: 153px; width: 228px; list-style: none;
    font-size: 11.5px;
  }
  .classic-list li {
    display: flex; height: 19.8px; align-items: center;
    border-bottom: 1px solid var(--rule);
  }
  .classic-list li:last-child { border-bottom: none; }
  .classic-list .name { width: 145px; }
  .classic-list .price { font-weight: 700; width: 44px; }

  .specialty-list {
    position: absolute; left: 19px; top: 349px; width: 452px; list-style: none;
  }
  .specialty-list li {
    display: flex; justify-content: space-between; align-items: center;
    height: 40.2px; padding-left: 2px;
    border-bottom: 1px solid var(--rule);
  }
  .specialty-list li:last-child { border-bottom: none; }
  .item-name { font-weight: 700; font-size: 11px; line-height: 1.25; }
  .item-desc { font-size: 11px; line-height: 1.25; }
  .prices { color: var(--brand-red); font-weight: 700; font-size: 11px; white-space: nowrap; word-spacing: 8px; }

  .front-footer {
    position: absolute; left: 0; bottom: 0; width: 100%; height: 83px;
    background: var(--brand-red); color: var(--white);
    display: flex; align-items: center; justify-content: center; text-align: center;
    font-size: 14.5px; line-height: 1.25; padding-top: 4px;
  }

  /* Back */
  .menu-list {
    position: absolute; left: 21px; top: 24px; width: 448px; list-style: none;
  }
  .menu-list li {
    display: flex; justify-content: space-between; align-items: flex-start;
    height: 35.8px; padding-top: 1px;
    border-bottom: 1px solid var(--rule);
  }
  .menu-list li.tall { height: 47.5px; }
  .menu-list li:last-child { border-bottom: none; }
  .menu-list .item-name { font-size: 10px; }
  .menu-list .item-desc { font-size: 9.6px; }
  .menu-list .prices { font-size: 11px; line-height: 1.1; text-align: right; }

  .back-footer {
    position: absolute; left: 0; bottom: 0; width: 100%; height: 87px;
    background: var(--brand-red); color: var(--white);
  }
  .contact {
    position: absolute; left: 23px; top: 6px; font-size: 9.8px; line-height: 1.22;
  }
  .contact .web { font-weight: 700; }
  .back-footer .wordmark {
    color: var(--white); left: 332px; top: 13px; font-size: 32px;
  }
  .back-footer .wordmark .line-two { padding-left: 22px; }
</style>
</head>
<body>
<div class="canvas">

  <section class="page page--front">
    <div class="wordmark"><span>CALDER</span><span class="line-two">PIZZA</span></div>
    <div class="pizza-photo" role="img" aria-label="Photo of a pepperoni pizza with black olives and tomatoes, slices pulled apart"></div>

    <h2 class="section-title section-title--classic">Classic Take-Out Pizza - 8" &amp; 13"</h2>
    <ul class="classic-list">
      <li><span class="name">Pepperoni &amp; Mushroom</span><span class="price">$12.99</span><span class="price">$30.95</span></li>
      <li><span class="name">Pepperoni</span><span class="price">$11.99</span><span class="price">$29.95</span></li>
      <li><span class="name">Hawaiian</span><span class="price">$12.99</span><span class="price">$30.95</span></li>
      <li><span class="name">Beef &amp; Mushroom</span><span class="price">$13.49</span><span class="price">$32.95</span></li>
      <li><span class="name">Pepperoni &amp; Ham</span><span class="price">$12.99</span><span class="price">$30.95</span></li>
      <li><span class="name">Ham &amp; Mushroom</span><span class="price">$12.99</span><span class="price">$30.95</span></li>
      <li><span class="name">Beef &amp; Onion</span><span class="price">$13.49</span><span class="price">$32.95</span></li>
      <li><span class="name">Cheese</span><span class="price">$11.99</span><span class="price">$29.95</span></li>
    </ul>

    <h2 class="section-title section-title--specialty">Specialty Take-Out Pizza- 8" &amp; 13"</h2>
    <ul class="specialty-list">
      <li><div><div class="item-name">All Meat</div><div class="item-desc">Pepperoni, Beef &amp; Smoked Ham</div></div><span class="prices">$14.99 $35.95</span></li>
      <li><div><div class="item-name">Double Pepperoni</div><div class="item-desc">Loads of Pepperoni</div></div><span class="prices">$13.49 $32.95</span></li>
      <li><div><div class="item-name">Hot Honey Pepperoni</div><div class="item-desc">Double Pepperoni and drizzled with Hot Honey</div></div><span class="prices">$14.49 $34.95</span></li>
      <li><div><div class="item-name">Hawaiian Heat</div><div class="item-desc">Smoked Ham, Pineapple and Banana Peppers</div></div><span class="prices">$13.49 $32.95</span></li>
      <li><div><div class="item-name">Four Cheese</div><div class="item-desc">Mozzarella, Feta, Romano and Cheddar Cheese</div></div><span class="prices">$13.49 $32.95</span></li>
      <li><div><div class="item-name">Montreal</div><div class="item-desc">Pepperoni &amp; Double Smoked Bacon</div></div><span class="prices">$13.49 $32.95</span></li>
      <li><div><div class="item-name">Supreme</div><div class="item-desc">Pepperoni, Mushrooms &amp; Green Peppers</div></div><span class="prices">$13.49 $32.95</span></li>
      <li><div><div class="item-name">Canadian</div><div class="item-desc">Pepperoni, Mushrooms &amp; Ham</div></div><span class="prices">$13.49 $32.95</span></li>
    </ul>

    <footer class="front-footer">
      <p>All of our pizzas are prepared fresh everyday using<br>only the finest mozzarella blend and ingredients.</p>
    </footer>
  </section>

  <section class="page page--back">
    <ul class="menu-list">
      <li><div><div class="item-name">BBQ Chicken</div><div class="item-desc">Chicken Breast, Hickory BBQ Sauce &amp; Red Onions</div></div><span class="prices">$13.99 $33.95</span></li>
      <li><div><div class="item-name">BBQ Chicken Plus</div><div class="item-desc">Chicken Breast, Hickory BBQ Sauce, Red Onions &amp; Cilantro</div></div><span class="prices">$14.79 $34.95</span></li>
      <li><div><div class="item-name">Spicy BBQ Chicken</div><div class="item-desc">Chicken Breast, Hickory BBQ Sauce, Red Onions &amp; Banana Peppers</div></div><span class="prices">$14.49 $35.95</span></li>
      <li><div><div class="item-name">Sweet Chili Chicken</div><div class="item-desc">Chicken Breast, Pineapple, Red Onions &amp; Sweet Chili Sauce</div></div><span class="prices">$14.49 $35.95</span></li>
      <li><div><div class="item-name">Chicken Club</div><div class="item-desc">Chicken Breast, Double Smoked Bacon, Red Onions and Tomatoes</div></div><span class="prices">$14.79 $35.95</span></li>
      <li><div><div class="item-name">Athenean</div><div class="item-desc">Chicken Breast, Spinach, Feta Cheese and Tomato</div></div><span class="prices">$14.49 $34.95</span></li>
      <li class="tall"><div><div class="item-name">Greek Supreme</div><div class="item-desc">Chicken Breast, Feta Cheese, Tomato, Green Pepper,<br>Red Onions &amp; Black Olives</div></div><span class="prices">$14.49 $34.95</span></li>
      <li><div><div class="item-name">Mediterranean Chicken</div><div class="item-desc">Seasoned Chicken Breast, Tomatoes, Red Onions and Feta Cheese</div></div><span class="prices">$14.79 $35.95</span></li>
      <li><div><div class="item-name">Original Spinach</div><div class="item-desc">Spinach &amp; Feta Cheese</div></div><span class="prices">$13.49 $32.95</span></li>
      <li><div><div class="item-name">Zeus</div><div class="item-desc">Spinach, Feta Cheese and Tomatoes</div></div><span class="prices">$13.95 $33.95</span></li>
      <li><div><div class="item-name">Greek</div><div class="item-desc">Feta Cheese, Tomato, Green Peppers, Red Onions and Black Olives</div></div><span class="prices">$13.99 $33.95</span></li>
      <li><div><div class="item-name">Vegetarian</div><div class="item-desc">Mushrooms, Tomatoes, Green Peppers and Black Olives</div></div><span class="prices">$13.49 $32.95</span></li>
      <li><div><div class="item-name">Veggie Delight</div><div class="item-desc">Mushrooms, Tomatoes, Green Peppers, Black Olives &amp; Onions</div></div><span class="prices">$13.95 $33.95</span></li>
      <li class="tall"><div><div class="item-name">Deluxe</div><div class="item-desc">Pepperoni, Mushrooms, Ham, Tomatoes, Green Peppers<br>and Red Onions</div></div><span class="prices">$14.49 $34.95</span></li>
      <li><div><div class="item-name">Calder Special</div><div class="item-desc">Pepperoni, Mushrooms, Ham, Green Peppers and Black Olives</div></div><span class="prices">$14.49 $34.95</span></li>
      <li class="tall"><div><div class="item-name">Dill Pickle</div><div class="item-desc">Crispy Dill Pickles, Fresh Dill with our cream based garlic sauce.<br>Served with or without bacon</div></div><span class="prices">$13.49 $32.95<br>$14.49 $35.95</span></li>
      <li><div><div class="item-name">BBQ Pulled Pork</div><div class="item-desc">Pulled Pork, Red Onions, Red Peppers and Cilantro</div></div><span class="prices">$14.49 $35.95</span></li>
    </ul>

    <footer class="back-footer">
      <address class="contact" style="font-style: normal;">
        Fenwick Ridge Plaza 417<br>
        318 9 Avenue SW<br>
        -<br>
        Visit our website for our complete<br>
        &nbsp;appetizer, pasta, salad and catering menu<br>
        <span class="web">www.calderpizza.ca</span>
      </address>
      <div class="wordmark"><span>CALDER</span><span class="line-two">PIZZA</span></div>
    </footer>
  </section>

</div>
</body>
</html>
```